Ductless Mini Split Business Website

Amber Kite Services is looking to design an eye catching educational website about installing Ductless mini splits.

Similar to this company.
https://www.cedarcoolair.com/

```html
<!DOCTYPE html>
<html lang="en">
<head>
<meta charset="utf-8">
<title>Amber Kite Services – Ductless Experts</title>
<link href="https://fonts.googleapis.com/css2?family=Playfair+Display:wght@700&family=Montserrat:ital,wght@0,300;0,400;0,500;0,600;1,400&display=swap" rel="stylesheet">
<style>
:root{
  --teal:#0f7f87;
  --teal-dark:#0b6970;
  --yellow:#ffd400;
  --ink:#1d1d1d;
  --muted:#8a8a8a;
  --light:#f4f4f4;
  --dark:#2b2b2b;
  --white:#ffffff;
}
*{box-sizing:border-box;margin:0;padding:0}
html,body{width:1200px;height:3699px;overflow:hidden}
body{position:relative;background:var(--white);font-family:"Montserrat",sans-serif;color:var(--ink)}
.abs{position:absolute}
.serif{font-family:"Playfair Display",serif;font-weight:700}

/* header */
.topbar{left:617px;top:0;width:583px;height:32px;background:var(--yellow);clip-path:polygon(28px 0,100% 0,100% 100%,0 100%);font-size:12px;color:var(--white);display:flex;align-items:center;padding-left:60px;gap:14px}
.topbar b{font-weight:400;color:var(--teal)}
.brand{left:89px;top:34px;display:flex;align-items:center;gap:10px;font-size:20px;font-weight:600;color:var(--ink)}
.brand i{width:16px;height:16px;border-radius:50%;background:var(--yellow);display:block}
.nav{left:478px;top:66px;display:flex;gap:40px;font-size:13px}
.nav .on{color:var(--yellow)}
.btn{display:flex;align-items:center;justify-content:center;border-radius:20px;font-size:12px}
.nav-cta{left:952px;top:60px;width:160px;height:32px;background:var(--teal);color:var(--white)}

/* hero */
.hero{left:0;top:119px;width:1200px;height:616px;background:linear-gradient(160deg,#a59e95 0%,#8e8a85 45%,#6e6a66 100%);clip-path:polygon(0 0,100% 0,100% 441px,0 100%)}
.hero-title{left:0;top:262px;width:1200px;text-align:center;font-size:40px;color:var(--white)}
.hero-sub{left:0;top:310px;width:1200px;text-align:center;font-size:32px;font-weight:300;color:var(--white)}
.hero-cta{left:505px;top:376px;width:190px;height:30px;background:var(--yellow);color:var(--ink)}
.card{top:560px;width:320px;height:199px;overflow:hidden}
.card .ph{width:100%;height:100%}
.card .tag{position:absolute;left:0;bottom:0;width:200px;height:32px;background:var(--teal);color:var(--white);font-size:16px;font-weight:600;padding:6px 0 0 32px;clip-path:polygon(0 0,85% 0,100% 100%,0 100%)}

/* about */
.about-box{left:208px;top:840px;width:479px;height:479px;background:var(--yellow);padding:60px 48px 0 48px}
.about-box h2{font-size:31px;color:var(--teal);margin-bottom:22px}
.about-lead{font-size:13.5px;font-weight:600;line-height:19px;margin-bottom:20px}
.about-box p.s{font-size:12px;line-height:15px;margin-bottom:16px}
.more{font-size:12.5px;color:var(--teal);margin-top:24px}
.about-img{left:687px;top:917px;width:305px;height:479px;background:linear-gradient(150deg,#d9d4cc,#7d8590 60%,#3d4a5c)}

/* sections */
.soft{left:0;top:1400px;width:1200px;height:700px;background:linear-gradient(180deg,#fafafa,#ececec 60%,#f6f6f6)}
.h-sec{left:0;width:1200px;text-align:center;font-size:32px;color:var(--teal)}
.divider{left:524px;width:152px;height:10px}
.feat{top:1578px;width:290px;text-align:center}
.feat h3{font-size:17.5px;font-weight:500;line-height:21px;margin:14px 0 24px}
.feat p{font-size:12px;color:var(--muted);line-height:17px}

/* request form */
.dark{left:0;top:2080px;width:1200px;height:1000px;background:linear-gradient(170deg,#3a3a3a,#262626 55%,#1f1f1f);clip-path:polygon(0 156px,100% 0,100% 870px,0 100%)}
.form{left:208px;top:1952px;width:784px;height:334px;background:var(--teal)}
.field{position:absolute;background:var(--white);border-radius:18px;font-size:12px;color:var(--teal);padding:11px 16px;height:38px}
.callstrip{left:928px;top:1952px;width:64px;height:334px;background:var(--yellow)}
.callstrip .vt{position:absolute;left:32px;top:48px;transform:rotate(90deg);transform-origin:0 0;white-space:nowrap;font-size:17px;font-weight:600;color:var(--teal);display:flex;align-items:center;gap:18px;margin-left:12px}

/* testimonial */
.avatar{left:556px;top:2468px;width:80px;height:80px;border-radius:50%;background:linear-gradient(180deg,#f1d88a,#e4b6a0);border:3px solid var(--white)}
.quote{left:260px;top:2568px;width:680px;text-align:center;font-size:15px;font-style:italic;line-height:24px;color:var(--white)}
.dots{left:566px;top:2792px;display:flex;gap:5px}
.dots i{width:9px;height:9px;border:1px solid var(--yellow);border-radius:50%;display:block}
.dots i.on{background:var(--yellow)}

/* appointment */
.appt-frame{left:115px;top:2905px;width:468px;height:341px;background:var(--yellow);border-radius:0 20px 0 0}
.appt-img{left:89px;top:2905px;width:480px;height:326px;border-radius:0 20px 0 20px;background:linear-gradient(130deg,#cfe1b8,#eaeae2 45%,#b9c1c6)}
.appt-r{right:88px;text-align:right}

/* footer */
.footer{left:0;top:3329px;width:1200px;height:370px;background:var(--teal);color:var(--white)}
.f-logo{left:89px;top:3427px;width:197px;height:115px;border-radius:50%;background:var(--white);display:flex;align-items:center;justify-content:center;font-size:15px;font-weight:600;color:var(--ink)}
.f-h{font-size:17px;font-weight:500;color:var(--white)}
.f-t{font-size:12px;line-height:18px;color:var(--white)}
.links{font-size:12px;line-height:24px;color:var(--white)}
.news{left:878px;top:3512px;width:235px;height:32px;border-radius:16px;background:var(--white);font-size:11px;color:var(--muted);padding:8px 16px}
.social{top:3641px;width:30px;height:30px;border-radius:50%;border:1.5px solid var(--yellow)}
</style>
</head>
<body>

<!-- header -->
<div class="abs topbar"><span>Call Us: <b>555-014-2290</b></span><span>|</span><span>Email: <b>service@amberkiteservices.com</b></span></div>
<div class="abs brand"><i></i>Amber Kite Services</div>
<nav class="abs nav"><span class="on">Home</span><span>About Us</span><span>Services</span><span>Reviews</span><span>Contact Us</span></nav>
<div class="abs btn nav-cta">Services Request</div>

<!-- hero -->
<div class="abs hero" role="img" aria-label="Photo of a woman relaxing on a sofa under a wall-mounted air conditioner"></div>
<div class="abs hero-title serif">Your Comfort is Our Goal</div>
<div class="abs hero-sub">Air conditioning resources for consumers</div>
<div class="abs btn hero-cta">Get a Free Consultation</div>

<div class="abs card" style="left:89px"><div class="ph" role="img" aria-label="Photo of an electrician working on wiring" style="background:linear-gradient(140deg,#d8d8dc,#8c8f98)"></div><div class="tag">Electrical</div></div>
<div class="abs card" style="left:439px"><div class="ph" role="img" aria-label="Photo of a man on a sofa under an HVAC unit" style="background:linear-gradient(140deg,#eeeeee,#7a7f80)"></div><div class="tag">HVAC</div></div>
<div class="abs card" style="left:791px"><div class="ph" role="img" aria-label="Photo of a plumber fixing a sink pipe" style="background:linear-gradient(140deg,#e2e2e2,#6f7686)"></div><div class="tag">Plumbing</div></div>

<!-- about -->
<div class="abs about-box">
  <h2 class="serif">About Us</h2>
  <p class="about-lead">Amber Kite Service Company provides HVAC, Plumbing and Electrical services to Carteret and Onslow County homes and businesses on the Crystal Coast of North Carolina. Our professional installation and repair technicians are ready to work hard for you every day!</p>
  <p class="s">We know your time is valuable and limited, so we work hard to fit into your schedule year-round for all of your HVAC, Electrical and plumbing needs.</p>
  <p class="s">Amber Kite makes taking care of your home easy by providing repairs, routine service, emergency service, installations, maintenance and more.</p>
  <p class="more">Discover More &nbsp;→</p>
</div>
<div class="abs about-img" role="img" aria-label="Photo of a technician explaining a repair to a homeowner"></div>

<!-- why choose -->
<div class="abs soft" role="img" aria-label="Faded photo of a modern house exterior"></div>
<h2 class="abs h-sec serif" style="top:1472px">Why Choose Amber Kite Service</h2>
<svg class="abs divider" style="top:1528px" viewBox="0 0 152 10"><line x1="0" y1="5" x2="66" y2="5" stroke="#ffd400"/><circle cx="76" cy="5" r="3.5" fill="#ffd400"/><line x1="86" y1="5" x2="152" y2="5" stroke="#ffd400"/></svg>

<div class="abs feat" style="left:105px">
  <svg width="60" height="60" viewBox="0 0 60 60" fill="none" stroke="#0f7f87" stroke-width="2"><rect x="10" y="4" width="34" height="50" rx="2"/><line x1="17" y1="16" x2="37" y2="16"/><line x1="17" y1="24" x2="37" y2="24" stroke="#ffd400"/><line x1="17" y1="32" x2="30" y2="32"/><path d="M18 44l5 5 9-10" stroke="#ffd400"/><path d="M40 38l14-18" stroke="#ffd400" stroke-width="3"/></svg>
  <h3>0% Financing for 60<br>months</h3>
  <p>It is a long established fact that a reade will be distracted by the readable content of a page when looking layout.</p>
</div>
<div class="abs feat" style="left:455px">
  <svg width="60" height="60" viewBox="0 0 60 60" fill="none" stroke="#0f7f87" stroke-width="2"><circle cx="32" cy="20" r="12" stroke="#ffd400"/><path d="M32 13v14M28 17h6a3 3 0 010 6h-4" stroke="#ffd400"/><path d="M4 42h10l10 6h18l12-8-4-3-12 5H28"/><path d="M14 42l8-5h10"/></svg>
  <h3>365 Day, Money Back<br>Guarantee</h3>
  <p>It is a long established fact that a reade will be distracted by the readable content of a page when looking layout.</p>
</div>
<div class="abs feat" style="left:806px">
  <svg width="60" height="60" viewBox="0 0 60 60" fill="none" stroke="#0f7f87" stroke-width="2"><rect x="8" y="28" width="10" height="24"/><path d="M18 30l10-16c2-4 8-2 7 3l-2 9h14c4 0 5 4 3 6 2 2 1 5-1 6 1 2 0 5-3 5H18" /><path d="M36 4l2 5M46 8l-3 4M26 6l3 4" stroke="#ffd400"/></svg>
  <h3>We Are the Experts in Ductless<br>Services</h3>
  <p>It is a long established fact that a reade will be distracted by the readable content of a page when looking layout.</p>
</div>

<!-- request -->
<h2 class="abs h-sec serif" style="top:1848px">Services Request</h2>
<svg class="abs divider" style="top:1903px" viewBox="0 0 152 10"><line x1="0" y1="5" x2="66" y2="5" stroke="#ffd400"/><circle cx="76" cy="5" r="3.5" fill="#ffd400"/><line x1="86" y1="5" x2="152" y2="5" stroke="#ffd400"/></svg>

<div class="abs dark" role="img" aria-label="Dark toned photo of a happy family on a sofa"></div>
<div class="abs form">
  <div class="field" style="left:64px;top:64px;width:288px">Name</div>
  <div class="field" style="left:64px;top:120px;width:288px">Phone</div>
  <div class="field" style="left:64px;top:177px;width:288px">Email</div>
  <div class="field" style="left:64px;top:232px;width:288px;display:flex;justify-content:space-between">Select Your Services<span>⌄</span></div>
  <div class="field" style="left:368px;top:64px;width:288px;height:150px">Message</div>
  <div class="field" style="left:368px;top:232px;width:288px;background:var(--yellow);color:var(--ink);text-align:center">Get a Free Consultation</div>
</div>
<div class="abs callstrip"><div class="vt">Call Now
  <svg width="18" height="18" viewBox="0 0 24 24" fill="none" stroke="#0f7f87" stroke-width="2"><path d="M5 3h4l2 5-3 2a12 12 0 006 6l2-3 5 2v4a2 2 0 01-2 2A17 17 0 013 5a2 2 0 012-2z"/></svg>
  555-014-2290</div></div>

<!-- testimonials -->
<h2 class="abs h-sec serif" style="top:2364px;color:var(--white)">Happy Clients Say</h2>
<svg class="abs divider" style="top:2418px" viewBox="0 0 152 10"><line x1="0" y1="5" x2="66" y2="5" stroke="#ffd400"/><circle cx="76" cy="5" r="3.5" fill="#ffd400"/><line x1="86" y1="5" x2="152" y2="5" stroke="#ffd400"/></svg>
<div class="abs avatar" role="img" aria-label="Client portrait photo"></div>
<p class="abs quote">Lorem ipsum dolor sit amet, consectetur adipisicing elit, sed do eiusmod tempor incididunt ut labore et dolore magna aliqua. Ut enim ad minim veniam, quis nostrud exercitation ullamco laboris nisi ut aliquip ex ea commodo consequat. Duis aute irure dolor in reprehenderit.</p>
<svg class="abs" style="left:440px;top:2684px" width="320" height="20" viewBox="0 0 320 20"><line x1="0" y1="12" x2="320" y2="12" stroke="#555"/><rect x="140" y="0" width="40" height="20" fill="#2a2a2a"/></svg>
<div class="abs" style="left:0;top:2683px;width:1200px;text-align:center;font-size:16px;color:var(--yellow);font-weight:600">66</div>
<div class="abs" style="left:0;top:2711px;width:1200px;text-align:center;font-size:14px;color:var(--teal)">Rowan Ellery</div>
<div class="abs" style="left:0;top:2732px;width:1200px;text-align:center;font-size:12px;color:var(--white)">Lorem Site</div>
<div class="abs dots"><i></i><i class="on"></i><i></i><i></i><i></i></div>

<!-- appointment -->
<div class="abs appt-frame"></div>
<div class="abs appt-img" role="img" aria-label="Photo of a smiling woman on a sofa holding a phone"></div>
<svg class="abs" style="left:1048px;top:3002px" width="64" height="62" viewBox="0 0 64 62" fill="none" stroke="#0f7f87" stroke-width="2.2"><rect x="2" y="8" width="60" height="52" rx="4"/><line x1="2" y1="20" x2="62" y2="20"/><line x1="16" y1="2" x2="16" y2="13"/><line x1="48" y1="2" x2="48" y2="13"/><g stroke="#ffd400"><circle cx="16" cy="32" r="3.5"/><circle cx="28" cy="32" r="3.5"/><circle cx="40" cy="32" r="3.5"/><circle cx="52" cy="32" r="3.5"/><circle cx="28" cy="44" r="3.5"/><circle cx="40" cy="44" r="3.5"/><circle cx="52" cy="44" r="3.5"/></g><circle cx="14" cy="46" r="8"/><path d="M10 46l3 3 5-5"/></svg>
<div class="abs appt-r" style="top:3088px;font-size:24px">Book Your Appointment</div>
<div class="abs appt-r" style="top:3122px;font-size:38px;font-weight:500;color:var(--teal)">Call: 555-014-2290</div>
<div class="abs btn" style="left:914px;top:3193px;width:198px;height:36px;background:var(--yellow)">Book Your Appointment</div>

<!-- footer -->
<footer class="abs footer"></footer>
<div class="abs f-logo">Amber Kite Services</div>
<div class="abs f-h" style="left:352px;top:3421px">Contact Us</div>
<div class="abs" style="left:352px;top:3455px;font-size:17px;font-weight:600"><span style="color:var(--yellow)">Call Us:</span> <span style="color:var(--white)">555-014-2290</span></div>
<div class="abs f-t" style="left:352px;top:3484px"><span style="color:var(--yellow)">e.</span> service@amberkiteservices.com</div>
<div class="abs f-t" style="left:352px;top:3524px">48 Harbor Ln. lorem 14001 Lorem City,<br>MB 10022</div>
<div class="abs f-h" style="left:703px;top:3421px">Quick Links</div>
<div class="abs links" style="left:703px;top:3450px">Home<br>About Us<br>Services<br>Reviews<br>Contact Us</div>
<div class="abs f-h" style="left:878px;top:3421px">Sign Up Newsletter</div>
<div class="abs f-t" style="left:878px;top:3455px;width:240px">There are many variations of passages lorem Ipsum available</div>
<div class="abs news">Enter your email ...</div>
<svg class="abs" style="left:1084px;top:3517px" width="22" height="22" viewBox="0 0 22 22"><circle cx="11" cy="11" r="11" fill="#ffd400"/><path d="M7 6l9 5-9 5 2-5z" fill="none" stroke="#0f7f87" stroke-width="1.4"/></svg>
<div class="abs" style="left:89px;top:3609px;width:1023px;height:1px;background:rgba(255,255,255,.25)"></div>
<div class="abs f-t" style="left:89px;top:3641px">© 2019 <span style="color:var(--yellow)">Amber Kite Service Company.</span> All Right Reserved</div>
<div class="abs social" style="left:880px"></div>
<div class="abs social" style="left:920px;background:var(--yellow)"></div>
<div class="abs social" style="left:958px"></div>
<div class="abs social" style="left:997px"></div>

</body>
</html>
```